We need a business card design for our website rvkventures.com. The Star Headline is rvkventures.com, in large lettering.We sell fashion rings of titanium, mirror pollished stainless steel, and related jewelry. Basically quality products competing with the high expense of gold.We have to portray honesty and trust, because thats who I am. I know marketing, but I am weak on colors and layout. 3D Gold curved edge letters are ok. No green and yellow.Black,Red,Purple and White in small amounts.No fancy Lettering.
No Rainbows in printing.
Our goal is selling our products online globally

Kind Regards Corwin Albury

Fashion

rvkventures.com
known for our ideal fit rings
email.corwinalburyptyltd@fernmail com

```html
<!DOCTYPE html>
<html lang="en">
<head>
<meta charset="utf-8">
<title>RVK Ventures business card</title>
<link rel="stylesheet" href="https://fonts.googleapis.com/css2?family=Oswald:wght@600&family=Libre+Baskerville:wght@700&family=Open+Sans:wght@300&display=swap">
<style>
  :root {
    --gold: #b07a1c;
    --gold-deep: #ad7006;
    --gold-dark: #5a3a08;
    --gold-light: #f3d27a;
    --cream: #e8d3a8;
    --band: #f7ecd0;
    --contact-text: #fbf1d6;
    --trim: #e0505a;
    --guide: #3cc4e0;
    --white: #ffffff;
  }
  * { margin: 0; padding: 0; box-sizing: border-box; }
  html, body { width: 961px; height: 1200px; overflow: hidden; background: var(--white); }
  .canvas { position: relative; width: 961px; height: 1200px; }
  .card { position: absolute; left: 0; width: 961px; height: 581px; overflow: hidden; border: 1px solid var(--trim); }
  .card--front { top: 0; background: linear-gradient(90deg, var(--gold) 0%, #c7974a 30%, var(--cream) 60%, var(--white) 90%); }
  .card--back { top: 618px; height: 582px; background: var(--white); }
  .guide { position: absolute; left: 21px; top: 22px; right: 21px; bottom: 21px; border: 1px solid var(--guide); pointer-events: none; }
  .web-band { position: absolute; left: 0; top: 222px; width: 480px; height: 138px; background: var(--band); }
  .website {
    position: absolute; left: 37px; top: 262px; width: 384px; white-space: nowrap;
    font-family: "Oswald", sans-serif; font-weight: 600; font-size: 41px; line-height: 1;
    color: var(--gold); text-transform: uppercase;
    text-shadow: -1px -1px 0 var(--gold-dark), 1px 1px 0 var(--gold-light);
  }
  .tagline {
    position: absolute; left: 0; top: 395px; width: 418px; text-align: right;
    font-family: "Libre Baskerville", serif; font-weight: 700; font-size: 33px; line-height: 58px;
    color: var(--gold); text-shadow: -1px -1px 0 var(--gold-dark), 1px 1px 0 var(--gold-light);
  }
  .photo { position: absolute; }
  .photo--eagle-ring { left: 531px; top: 98px; width: 362px; height: 389px; border-radius: 48%;
    background: radial-gradient(ellipse at 45% 45%, #dedede 0%, #b4b4b4 45%, #8a8a8a 68%, rgba(255,255,255,0) 71%); }
  .photo--band-ring { left: 119px; top: 190px; width: 185px; height: 201px; border-radius: 50%;
    background: radial-gradient(ellipse at 50% 50%, #e9c24a 0%, #c9a02e 45%, #bfbfbf 62%, rgba(255,255,255,0) 71%); }
  .contact-panel { position: absolute; left: 396px; top: 176px; width: 565px; height: 230px; background: var(--gold-deep); }
  .contact {
    position: absolute; left: 77px; top: 24px;
    font-family: "Open Sans", sans-serif; font-weight: 300; font-size: 28px; line-height: 30px;
    color: var(--contact-text); white-space: nowrap;
  }
  .contact__gap { height: 29px; }
</style>
</head>
<body>
<div class="canvas">
  <section class="card card--front">
    <div class="web-band"></div>
    <p class="website">www.rvkventures.com</p>
    <p class="tagline">Known for our ideal<br>fit rings</p>
    <div class="photo photo--eagle-ring" role="img" aria-label="Polished stainless steel eagle ring with banner engraving"></div>
    <div class="guide"></div>
  </section>

  <section class="card card--back">
    <div class="photo photo--band-ring" role="img" aria-label="Gold and silver titanium band ring with screw details"></div>
    <div class="contact-panel">
      <div class="contact">
        <p>Email</p>
        <p>corwinalburyptyltd@fernmail.com</p>
        <div class="contact__gap"></div>
        <p>Fax</p>
        <p>+61 02 5550 3184 (International)</p>
        <p>02 5550 3184 (Local)</p>
      </div>
    </div>
    <div class="guide"></div>
  </section>
</div>
</body>
</html>
```